Office Building Banner

Need a 4x8 vinyl banner made for our office/storage headquarters. Our branded colors and logo can be taken from our website, www.brightcrestroofingtx.com. All other elements of our brand have not been decided on yet, so you have creative autonomy there. Our location faces a busy highway in Seguin, Texas, so the banner needs to have our contact information and full name clearly seen from a bit away's away, hope that makes sense. Our company wants to convey attributes of strength, loyalty, protection - basically emulating the qualities of a wolf and his pack. I have uploaded a few items we have been using to date, but as you can see, graphic design is not our forte.

```html
<!DOCTYPE html>
<html lang="en">
<head>
<meta charset="utf-8">
<title>Brightcrest Roofing &amp; Renovations Banner</title>
<link href="https://fonts.googleapis.com/css2?family=Poppins:wght@600;700;800&display=swap" rel="stylesheet">
<style>
  :root {
    --orange: #f28123;
    --black: #0d0d0d;
    --white: #ffffff;
    --grass: #5f9a3a;
    --sky: #b8c9d8;
  }
  * { margin: 0; padding: 0; box-sizing: border-box; }
  html, body { width: 1200px; height: 741px; overflow: hidden; background: var(--white); }
  .banner {
    position: relative; width: 1200px; height: 741px; overflow: hidden;
    background: var(--white); font-family: "Poppins", sans-serif;
  }
  .banner-shapes { position: absolute; inset: 0; }
  .footer-band { position: absolute; left: 0; right: 0; bottom: 0; height: 40px; background: var(--black); }

  .brand { position: absolute; left: 40px; top: 150px; width: 360px; display: flex; align-items: center; gap: 14px; }
  .brand-dot { width: 46px; height: 46px; border-radius: 50%; background: var(--orange); flex: none; }
  .brand-name { font-weight: 800; color: var(--black); font-size: 30px; line-height: 1.1; letter-spacing: 0.5px; }

  .headline { position: absolute; left: 40px; top: 405px; font-weight: 800; line-height: 1.05; transform: rotate(-2deg); transform-origin: left top; }
  .headline span { display: block; font-size: 50px; letter-spacing: -1px; }
  .headline .dark { color: var(--black); }
  .headline .accent { color: var(--orange); }
  .address { position: absolute; left: 42px; top: 632px; font-weight: 700; font-size: 25px; color: var(--black); transform: rotate(-2deg); transform-origin: left top; }

  .values { position: absolute; left: 470px; top: 0; width: 330px; height: 385px; }
  .value { position: absolute; display: flex; align-items: center; gap: 18px; color: var(--white); font-weight: 700; font-size: 24px; letter-spacing: 1px; }
  .value svg { width: 50px; height: 50px; flex: none; }
  .value-strength { left: 90px; top: 40px; }
  .value-loyalty { left: 50px; top: 165px; }
  .value-protection { left: 90px; top: 290px; }

  .contact { position: absolute; left: 590px; top: 400px; width: 560px; text-align: center; transform: rotate(-2deg); }
  .contact-call { font-weight: 800; font-size: 50px; color: var(--black); line-height: 1.05; letter-spacing: -1px; }
  .contact-phone { display: flex; justify-content: center; align-items: center; gap: 14px; font-weight: 800; font-size: 58px; color: var(--black); line-height: 1.1; }
  .contact-phone svg { width: 50px; height: 50px; }
  .contact-line { font-weight: 600; font-size: 27px; color: var(--white); line-height: 1.45; }
</style>
</head>
<body>
<main class="banner">
  <svg class="banner-shapes" width="1200" height="741" viewBox="0 0 1200 741" aria-hidden="true">
    <defs>
      <linearGradient id="house-photo" x1="0" y1="0" x2="0" y2="1">
        <stop offset="0" stop-color="#c9d6e2"/>
        <stop offset="0.55" stop-color="#8a7e72"/>
        <stop offset="0.7" stop-color="#6e9a45"/>
        <stop offset="1" stop-color="#4f8a2e"/>
      </linearGradient>
    </defs>
    <polygon class="chevron-orange" fill="var(--orange)" points="415,0 470,0 405,192 485,385 430,385 350,192"/>
    <polygon class="panel-black" fill="var(--black)" points="490,0 830,0 760,192 840,385 540,385 460,192"/>
    <polygon class="arrow-black" fill="var(--black)" points="1140,0 1200,0 1200,385 1165,385 1090,192"/>
    <polygon class="panel-contact" fill="var(--orange)" points="600,385 1180,385 1110,700 530,700"/>
  </svg>
  <svg class="house-photo" style="position:absolute;left:0;top:0" width="1200" height="741" viewBox="0 0 1200 741" role="img" aria-label="Photo of a two-storey suburban house with a brown shingle roof and green lawn">
    <polygon fill="url(#house-photo)" points="850,0 1120,0 1070,192 1150,360 860,360 780,192"/>
  </svg>
  <div class="footer-band"></div>

  <div class="brand">
    <span class="brand-dot"></span>
    <span class="brand-name">BRIGHTCREST ROOFING &amp; RENOVATIONS LLC</span>
  </div>

  <section class="values">
    <svg style="position:absolute;left:0;top:0" width="330" height="385" viewBox="0 0 330 385" aria-hidden="true">
      <line x1="50" y1="130" x2="280" y2="118" stroke="var(--orange)" stroke-width="3"/>
      <line x1="45" y1="255" x2="280" y2="243" stroke="var(--orange)" stroke-width="3"/>
    </svg>
    <div class="value value-strength">
      <svg viewBox="0 0 50 50" fill="none" stroke="var(--orange)" stroke-width="3"><circle cx="25" cy="25" r="20"/><path d="M15 30 L25 14 L35 30 Z"/></svg>
      STRENGTH
    </div>
    <div class="value value-loyalty">
      <svg viewBox="0 0 50 50" fill="none" stroke="var(--orange)" stroke-width="3"><circle cx="25" cy="25" r="20"/><circle cx="25" cy="25" r="9"/></svg>
      LOYALTY
    </div>
    <div class="value value-protection">
      <svg viewBox="0 0 50 50" fill="none" stroke="var(--orange)" stroke-width="3" stroke-linejoin="round"><path d="M25 4 L43 11 V24 C43 36 34 43 25 47 C16 43 7 36 7 24 V11 Z"/><path d="M17 25 L23 31 L34 19"/></svg>
      PROTECTION
    </div>
  </section>

  <h1 class="headline">
    <span class="dark">LOCAL ROOFING</span>
    <span class="accent">COMPANY SERVING</span>
    <span class="accent">GREATER, TX</span>
  </h1>
  <p class="address">P.O. Box 4410 Cedar Park TX 78613</p>

  <section class="contact">
    <p class="contact-call">CALL US TODAY</p>
    <p class="contact-phone">
      <svg viewBox="0 0 50 50"><circle cx="25" cy="25" r="24" fill="var(--black)"/><path d="M17 13 L22 13 L24 20 L21 22 C22.5 26 24 27.5 28 29 L30 26 L37 28 L37 33 C37 35 35 37 33 37 C23 36 14 27 13 17 C13 15 15 13 17 13 Z" fill="var(--orange)"/></svg>
      512-555-0148
    </p>
    <p class="contact-line">brightcrestroofingtx@gmail.com</p>
    <p class="contact-line">www.brightcrestroofingtx.com</p>
  </section>
</main>
</body>
</html>
```